Audio/ Video Packaging Design for a Technology company.

We need a packaging design for a bag that is 7" wide and 10" high. The design will be for a new line of audio/video products. We would like to see designs that represent a superior quality product that provides a pure connection. We want the equivalent of a nice retail bag that you would find in a store like Crest Mart. It should be a maximum of three colors. We really want something sharp, professional and eye catching, not whimsical or cartoonish. I've included a couple of examples below. I don't really like the designs of the bags, but I want you to see examples of what I'm looking for.

The company logo, which is uploaded, should be on the design. The words "audio and video products" should be either underneath the logo or to the side. Also, somewhere on the bag, we would like the words "For a Pure Connection"

The winner of this contest will likely get the opportunity for additional work as we have more products ready to launch.

Target Market(s)

resellers, consumers - men 25-60

Industry/Entity Type

It Company

Requirements
Must have
• It should be a maximum of three colors. We really want something sharp, professional and eye catching, not whimsical or cartoonish
Nice to have
• Eye-catching design. Utilize the entire bag but don't make it too busy.
Should not have
• Whimsical, cartoonish

```html
<!DOCTYPE html>
<html lang="en">
<head>
<meta charset="utf-8">
<title>Verant Audio &amp; Video Retail Bag</title>
<link rel="stylesheet" href="https://fonts.googleapis.com/css2?family=Open+Sans:wght@400;600&display=swap">
<style>
  :root {
    --backdrop: #665e58;
    --bag: #f1f1f1;
    --line: #2b2b2b;
    --blue: #43ace3;
    --ink: #2e343c;
  }
  html, body {
    margin: 0;
    padding: 0;
    width: 1200px;
    height: 1200px;
    overflow: hidden;
    background: var(--backdrop);
    font-family: "Open Sans", sans-serif;
  }
  .canvas {
    position: relative;
    width: 1200px;
    height: 1200px;
  }
  .bag-outline {
    position: absolute;
    left: 0;
    top: 0;
  }
  .pattern-field {
    position: absolute;
    left: 294px;
    top: 248px;
    width: 592px;
    height: 847px;
    background:
      radial-gradient(circle at 20% 15%, rgba(67,172,227,0.55) 0, rgba(67,172,227,0) 22%),
      radial-gradient(circle at 80% 45%, rgba(67,172,227,0.5) 0, rgba(67,172,227,0) 26%),
      radial-gradient(circle at 35% 80%, rgba(67,172,227,0.55) 0, rgba(67,172,227,0) 26%),
      radial-gradient(circle at 85% 90%, rgba(67,172,227,0.45) 0, rgba(67,172,227,0) 20%),
      linear-gradient(135deg, #d7ebf6 0%, #eef3f6 50%, #d7ebf6 100%);
  }
  .diagonal {
    position: absolute;
    transform: translate(-50%, -50%) rotate(-45deg);
    transform-origin: center;
    white-space: nowrap;
    color: var(--ink);
  }
  .product-line {
    left: 410px;
    top: 566px;
    font-size: 24px;
    line-height: 28px;
    text-align: center;
    color: #111;
  }
  .brand {
    left: 596px;
    top: 566px;
    display: flex;
    align-items: center;
    gap: 22px;
  }
  .brand-mark {
    width: 46px;
    height: 46px;
    background: var(--blue);
  }
  .brand-name {
    font-size: 96px;
    font-weight: 400;
    letter-spacing: 6px;
    line-height: 1;
    color: var(--ink);
  }
  .tagline {
    left: 660px;
    top: 612px;
    font-size: 27px;
    color: #111;
  }
</style>
</head>
<body>
<main class="canvas">
  <svg class="bag-outline" width="1200" height="1200" viewBox="0 0 1200 1200">
    <rect x="277" y="71" width="625" height="1057" rx="18" fill="var(--bag)" stroke="var(--line)" stroke-width="1.2"/>
    <path d="M514 118 H558 V108 Q558 102 564 102 H616 Q622 102 622 108 V118 H667 Q677 118 677 128 V145 Q677 155 667 155 H514 Q504 155 504 145 V128 Q504 118 514 118 Z" fill="var(--bag)" stroke="var(--line)" stroke-width="1.2"/>
    <line x1="277" y1="197" x2="902" y2="197" stroke="#555" stroke-width="1"/>
    <line x1="277" y1="205" x2="902" y2="205" stroke="#777" stroke-width="1"/>
    <line x1="277" y1="214" x2="902" y2="214" stroke="#555" stroke-width="1"/>
    <line x1="277" y1="228" x2="902" y2="228" stroke="#555" stroke-width="1"/>
    <rect x="294" y="248" width="592" height="847" fill="none" stroke="var(--line)" stroke-width="1"/>
  </svg>

  <div class="pattern-field" role="img" aria-label="Decorative pattern of blue connected dots and rounded links on a light grey field"></div>

  <div class="diagonal product-line">audio<br>and video<br>products</div>

  <div class="diagonal brand">
    <span class="brand-mark"></span>
    <span class="brand-name">VERANT</span>
  </div>

  <div class="diagonal tagline">for a pure connection</div>
</main>
</body>
</html>
```